Velvet Fern Beauty Bar Business Card

We need a modern, elegant business card design for our new beauty bar located in La Quinta, CA. The card should feel premium yet approachable, reflecting our brand identity: warm, stylish, and confidence-boosting.

Use our existing Velvet Fern Beauty Bar logo (to be provided as vector file).

Colors: Black, White, Blush / Nude accents, and Gold (metallic or foil effect if possible).

Typography: Clean sans-serif for clarity, with optional elegant script accent.
Design Style

Minimalist and modern with plenty of white space.

Premium look with a beauty/lifestyle feel (not overly corporate).

Option to explore vertical or horizontal orientation.

Rounded corners welcome, but not required.

Additional Notes

Design should print well in both matte and glossy finishes.

Please present mockups with both light and dark backgrounds.

Keep overall feel sleek, feminine, and high-end while still being approachable.

```html
<!DOCTYPE html>
<html lang="en">
<head>
<meta charset="utf-8">
<title>Velvet Fern Beauty Bar – Business Card</title>
<link href="https://fonts.googleapis.com/css2?family=Josefin+Sans:wght@400&family=Montserrat:wght@400;600&display=swap" rel="stylesheet">
<style>
  :root{
    --page:#ecebe8;
    --card:#2f2f31;
    --gold:#d2a92b;
    --soft-grey:#8d8d90;
    --text-light:#c9c9cc;
  }
  *{margin:0;padding:0;box-sizing:border-box}
  html,body{width:1200px;height:891px;overflow:hidden;background:var(--page)}
  body{position:relative;font-family:"Montserrat",sans-serif}

  .card{
    position:absolute;width:600px;height:343px;background:var(--card);
    border-radius:6px;box-shadow:0 10px 28px rgba(0,0,0,.25);overflow:hidden;
  }
  .card--front{left:520px;top:110px}
  .card--back{left:80px;top:440px}

  .pattern{position:absolute;inset:0;
    background:radial-gradient(circle at 50% 50%, #343437 0%, var(--card) 70%)}

  .brand-name{
    position:absolute;display:flex;align-items:center;
    color:var(--gold);font-family:"Josefin Sans",sans-serif;font-weight:400;
    white-space:nowrap;line-height:1;
  }
  .brand-name__dot{border-radius:50%;background:var(--gold);flex:none}

  .card--front .brand-name{left:0;right:0;top:154px;justify-content:center;gap:14px;font-size:36px}
  .card--front .brand-name__dot{width:14px;height:14px}

  .swoosh-area{position:absolute;left:0;top:0;width:330px;height:343px;
    background:linear-gradient(135deg,#3b3b3e 0%,#2f2f31 60%,#4a4a4d 100%);
    clip-path:ellipse(70% 55% at 20% 40%)}

  .card--back .brand-name{left:300px;top:178px;gap:8px;font-size:20px}
  .card--back .brand-name__dot{width:8px;height:8px}

  .person{position:absolute;left:300px;top:228px;color:var(--text-light)}
  .person__name{font-weight:600;font-size:16px;letter-spacing:.02em}
  .person__role{font-size:11px;color:var(--soft-grey);margin-bottom:8px}
  .contact{list-style:none;font-size:11.5px;color:var(--text-light)}
  .contact li{display:flex;align-items:center;gap:8px;height:19px}
  .contact svg{width:11px;height:11px;fill:none;stroke:var(--soft-grey);stroke-width:1.5}
</style>
</head>
<body>

<section class="card card--front" aria-label="Card front">
  <div class="pattern" role="img" aria-label="Faint embossed repeating pattern of small brand marks"></div>
  <p class="brand-name"><span class="brand-name__dot"></span>Velvet Fern Beauty Bar</p>
</section>

<section class="card card--back" aria-label="Card back">
  <div class="swoosh-area" role="img" aria-label="Large faint tonal decorative curve"></div>
  <p class="brand-name"><span class="brand-name__dot"></span>Velvet Fern Beauty Bar</p>
  <div class="person">
    <p class="person__name">YOURNAME</p>
    <p class="person__role">Position</p>
    <ul class="contact">
      <li><svg viewBox="0 0 12 12"><path d="M3 1.5l1.5 2.5-1 1c.6 1.3 1.3 2 2.5 2.5l1-1L9.5 8 8.5 10C5 9.5 2.5 7 2 3.5z"/></svg>123-456-2100</li>
      <li><svg viewBox="0 0 12 12"><rect x="1" y="2.5" width="10" height="7" rx="1"/><path d="M1 3l5 3.5L11 3"/></svg>youremail@example.com</li>
      <li><svg viewBox="0 0 12 12"><circle cx="6" cy="6" r="4.8"/><path d="M1.2 6h9.6M6 1.2c-2.4 3-2.4 6.6 0 9.6M6 1.2c2.4 3 2.4 6.6 0 9.6"/></svg>www.yourwebsite.com</li>
    </ul>
  </div>
</section>

</body>
</html>
```